Take my logo and make me some cool looking business cards

I've got a logo that we've trademarked so you can't change the logo but you can change it's color combo and find a fun way to incorporate it into a new business card design that is fresh, stylish, and can be applied to some cool medium cost materials (plastic, wood, metal, etc). Basically, we're looking for business cards that stand out in a good way.
Here's the logo we're currently using:
Thanks to everyone that has submitted designs. We've narrowed down to the top 4 designs and tried to eliminate old versions or designs that just didn't match our vision as quickly as we could. We don't plan on keeping this open for the full 9 days; we plan on selecting a design in the next 48 hours; with the goal of having something in the hands of a printer, preferably plastic printer, by Thursday AM Pacific Time.
Business
- must include our existing logo

```html
<!DOCTYPE html>
<html lang="en">
<head>
<meta charset="utf-8">
<title>Lanyard Business Cards</title>
<link rel="stylesheet" href="https://fonts.googleapis.com/css2?family=Arimo:wght@400;700&display=swap">
<style>
  :root {
    --backdrop: #9d9e9d;
    --card-dark: #1c1a17;
    --card-light: #ffffff;
    --ink-light: #ffffff;
    --ink-slate: #56648f;
    --accent-blue: #0a8fd6;
    --accent-teal: #1fb3c6;
    --tone-green: #6db33f;
    --tone-yellow: #e8e21a;
    --tone-orange: #ee6a24;
    --tone-sky: #bfe3f0;
    --tone-slate: #5a6a94;
    --tone-aqua: #4fbfcf;
    --tone-deep: #1298c4;
  }
  * { margin: 0; padding: 0; box-sizing: border-box; }
  html, body {
    width: 1200px;
    height: 901px;
    overflow: hidden;
    background: var(--backdrop);
    font-family: "Arimo", Arial, sans-serif;
  }
  .stage {
    position: relative;
    width: 1200px;
    height: 901px;
  }
  .card {
    position: absolute;
    width: 620px;
    height: 354px;
    overflow: hidden;
    box-shadow: 0 10px 24px rgba(0, 0, 0, 0.28);
  }
  .card--dark {
    left: 110px;
    top: 140px;
    background: var(--card-dark);
    color: var(--ink-light);
  }
  .card--light {
    left: 470px;
    top: 400px;
    background: var(--card-light);
    color: var(--ink-slate);
  }
  .brand-art {
    position: absolute;
    right: 0;
    top: 0;
    width: 300px;
    height: 240px;
    border-bottom-left-radius: 60px;
  }
  .card--dark .brand-art {
    background: linear-gradient(135deg, var(--tone-green) 0%, var(--accent-blue) 35%, var(--tone-orange) 60%, var(--tone-yellow) 82%, var(--tone-sky) 100%);
    opacity: 0.85;
  }
  .card--light .brand-art {
    background: linear-gradient(135deg, var(--tone-deep) 0%, var(--tone-aqua) 45%, var(--tone-slate) 100%);
    opacity: 0.8;
  }
  .wordmark {
    position: absolute;
    left: 80px;
    top: 150px;
    display: flex;
    align-items: center;
    gap: 12px;
    font-size: 38px;
    font-weight: 400;
    letter-spacing: 1px;
  }
  .wordmark__dot {
    width: 18px;
    height: 18px;
    border-radius: 50%;
  }
  .card--dark .wordmark__dot { background: var(--accent-blue); }
  .card--light .wordmark__dot { background: var(--accent-teal); }
  .contact {
    position: absolute;
    left: 120px;
    top: 236px;
    font-size: 15px;
    line-height: 1.25;
  }
  .contact__name {
    font-weight: 700;
  }
  .contact__role {
    margin-bottom: 10px;
  }
</style>
</head>
<body>
<main class="stage">
  <article class="card card--dark">
    <div class="brand-art" role="img" aria-label="Multicolour brand ribbon decoration area"></div>
    <div class="wordmark"><span>LANYARD</span><span class="wordmark__dot"></span></div>
    <div class="contact">
      <p class="contact__name">Daniel Marsh</p>
      <p class="contact__role">Director</p>
      <p>daniel@lanyard.com</p>
      <p>+1 000 000 0000</p>
      <p>www.lanyard.com</p>
    </div>
  </article>

  <article class="card card--light">
    <div class="brand-art" role="img" aria-label="Blue and teal brand ribbon decoration area"></div>
    <div class="wordmark"><span>LANYARD</span><span class="wordmark__dot"></span></div>
    <div class="contact">
      <p class="contact__name">Daniel Marsh</p>
      <p class="contact__role">Director</p>
      <p>daniel@lanyard.com</p>
      <p>+1 000 000 0000</p>
      <p>www.lanyard.com</p>
    </div>
  </article>
</main>
</body>
</html>
```